Software company specialized in data analytics and professional services

We need a landing page design for our business. It should include our logo design. It should have multiple sections :
- stylish head
- what we do (data analytics software, professional services)
- contact form

Target Market(s)

Companies, B2B

Industry/Entity Type

Data

Number of Pages Required

1 page

Font styles to use
Sans Serif

Requirements
Must have
• Dark theme
Should not have
• Gradients on buttons

```html
<!DOCTYPE html>
<html lang="en">
<head>
<meta charset="utf-8">
<title>Brightmere — Data Analytics &amp; Professional Services</title>
<link href="https://fonts.googleapis.com/css2?family=Manrope:wght@400;500;600;700;800&display=swap" rel="stylesheet">
<style>
:root{
  --bg:#150a3a;
  --bg-deep:#0f0830;
  --panel:#2a0c58;
  --magenta:#d9139f;
  --pink-label:#e0269f;
  --text:#ffffff;
  --muted:#c9bde0;
  --field:#1f0f4d;
}
*{box-sizing:border-box;margin:0;padding:0}
html,body{width:1200px;height:4743px;overflow:hidden}
body{background:linear-gradient(180deg,var(--bg) 0%,#1b0b45 40%,#3a0f62 48%,#1e0b4a 56%,#2a0c55 75%,var(--bg-deep) 82%,var(--bg-deep) 100%);font-family:"Manrope",sans-serif;color:var(--text);position:relative}
.abs{position:absolute}
.label{font-size:10px;letter-spacing:2px;font-weight:600;color:var(--pink-label);text-transform:uppercase}
.btn{display:inline-flex;align-items:center;gap:8px;background:var(--magenta);color:#fff;font-weight:700;font-size:13px;border-radius:24px;justify-content:center;text-decoration:none}
.brand{display:flex;align-items:center;gap:10px;font-weight:800;font-size:34px;color:var(--magenta);letter-spacing:1px}
.brand .dot{width:14px;height:14px;border-radius:50%;background:var(--magenta)}
.nav-links{top:32px;left:473px;display:flex;gap:34px;font-size:13px;font-weight:500}
.hero-panel{left:17px;top:83px;width:1164px;height:611px;border-radius:22px;background:linear-gradient(110deg,#8d168f 0%,#5a137f 45%,#3e1280 100%)}
.hero-title{font-size:46px;line-height:53px;font-weight:700;width:520px}
.para{font-size:13px;line-height:23px;color:var(--muted)}
.features{left:83px;top:552px;width:1032px;height:269px;border-radius:18px;background:var(--panel);display:grid;grid-template-columns:repeat(4,1fr);padding:56px 40px 0}
.feature{text-align:center;padding:0 12px}
.feature .ico{width:44px;height:44px;border-radius:50%;background:var(--magenta);margin:0 auto 28px;display:flex;align-items:center;justify-content:center}
.feature h3{font-size:13px;font-weight:700;margin-bottom:8px}
.feature p{font-size:12px;line-height:23px;color:var(--muted)}
h2{font-size:40px;font-weight:700;line-height:52px}
.ticks{list-style:none;font-size:12.5px;color:var(--muted)}
.ticks li{display:flex;align-items:center;gap:10px;height:32px}
.ticks li::before{content:"";width:15px;height:15px;border:1.5px solid var(--magenta);border-radius:50%;flex:none}
.cta{left:96px;top:2074px;width:1032px;height:342px;border-radius:22px;background:linear-gradient(120deg,#3a1075,#4a128a 60%,#5e18a6);text-align:center}
.works{left:83px;top:2650px;width:1032px;display:grid;grid-template-columns:1fr 1fr;gap:8px}
.tile{height:512px;position:relative;display:flex;flex-direction:column;justify-content:flex-end;align-items:center;padding-bottom:44px;text-align:center}
.tile h4{font-size:19px;font-weight:700}
.partners{left:96px;top:3782px;width:1010px;display:flex;justify-content:space-between}
.partners span{width:120px;height:34px;border-radius:8px;background:#4b2a7a;opacity:.8}
.contact-bg{left:0;top:3920px;width:1200px;height:823px;background:var(--bg-deep)}
.field-label{font-size:10.5px;color:var(--muted)}
.field{background:var(--field);border-radius:4px}
.social{display:flex;gap:14px}
.social span{width:26px;height:26px;border-radius:7px;background:var(--magenta)}
</style>
</head>
<body>

<div class="abs brand" style="left:83px;top:20px"><span>BRIGHTMERE</span><span class="dot"></span></div>
<nav class="abs nav-links"><span>Home</span><span>What We Do</span><span>Contact Us</span></nav>
<a class="abs btn" style="left:985px;top:22px;width:130px;height:40px">Get Started</a>

<section class="abs hero-panel"></section>
<div class="abs label" style="left:83px;top:152px">Brightmere</div>
<h1 class="abs hero-title" style="left:83px;top:180px">The Trusted Data Analytics and Professional Services</h1>
<p class="abs para" style="left:83px;top:369px;width:480px">Lorem ipsum dolor sit amet, consectetur adipiscing elit, sed do eiusmod tempor incididunt ut labore et dolore magna aliqua.</p>
<a class="abs btn" style="left:83px;top:441px;width:195px;height:44px">Find Best Service
<svg width="14" height="10" viewBox="0 0 14 10"><path d="M1 5h11M8 1l4 4-4 4" stroke="#fff" stroke-width="1.6" fill="none"/></svg></a>
<div class="abs" role="img" aria-label="Illustration of a businesswoman presenting floating data dashboards and charts" style="left:653px;top:150px;width:414px;height:400px;border-radius:18px;background:radial-gradient(circle at 60% 40%,#4d8bf0 0%,#3b55c8 35%,rgba(90,30,140,0) 70%)"></div>

<section class="abs features">
  <div class="feature"><div class="ico"><svg width="18" height="18"><circle cx="9" cy="9" r="6" stroke="#fff" stroke-width="1.6" fill="none"/></svg></div><h3>Advance Advisory Team</h3><p>Incididunt ut labore et dolore magna aliqua. Ut enim ad minim veniam.</p></div>
  <div class="feature"><div class="ico"><svg width="18" height="18"><circle cx="9" cy="9" r="6" stroke="#fff" stroke-width="1.6" fill="none"/><circle cx="9" cy="9" r="2" fill="#fff"/></svg></div><h3>Professional Consulting</h3><p>Ut enim ad minim veniam, quis nostrud exercitation ullamco laboris nisi ut aliquip.</p></div>
  <div class="feature"><div class="ico"><svg width="18" height="18"><rect x="3" y="3" width="12" height="12" rx="2" stroke="#fff" stroke-width="1.6" fill="none"/></svg></div><h3>24/7 Support Help Center</h3><p>Duis aute irure dolor in reprehenderit in voluptate velit esse cillum dolore.</p></div>
  <div class="feature"><div class="ico"><svg width="18" height="18"><path d="M4 3h10v12H4z" stroke="#fff" stroke-width="1.6" fill="none"/></svg></div><h3>Clients Service &amp; Operations</h3><p>Excepteur sint occaecat cupidatat non proident, sunt in culpa qui officia.</p></div>
</section>

<div class="abs" role="img" aria-label="Illustration of a woman at a laptop surrounded by analytics charts" style="left:83px;top:900px;width:506px;height:452px;border-radius:50%;background:radial-gradient(circle,#3a5fd6 0%,#22307e 45%,#1b1850 70%)"></div>
<div class="abs label" style="left:613px;top:982px">What We Do</div>
<h2 class="abs" style="left:613px;top:1016px">Data Analytics Software</h2>
<p class="abs para" style="left:613px;top:1096px;width:500px">Lorem ipsum dolor sit amet, consectetur adipiscing elit, sed do eiusmod tempor incididunt ut labore et dolore magna aliqua. Ut enim ad minim veniam, quis nostrud exercitation ullamco laboris nisi.</p>
<ul class="abs ticks" style="left:613px;top:1184px">
  <li>Ut enim ad minim veniam, quis nostrud exercitation.</li>
  <li>Lorem ipsum dolor sit amet, consectetur adipiscing elit.</li>
  <li>Ut enim ad minim veniam, quis nostrud exercitation.</li>
  <li>Lorem ipsum dolor sit amet, consectetur adipiscing elit.</li>
  <li>Ut enim ad minim veniam, quis nostrud exercitation.</li>
</ul>

<div class="abs label" style="left:83px;top:1576px">What We Do</div>
<h2 class="abs" style="left:83px;top:1610px">Professional Services</h2>
<p class="abs para" style="left:83px;top:1690px;width:500px">Lorem ipsum dolor sit amet, consectetur adipiscing elit, sed do eiusmod tempor incididunt ut labore et dolore magna aliqua. Ut enim ad minim veniam, quis nostrud exercitation ullamco laboris nisi.</p>
<ul class="abs ticks" style="left:83px;top:1777px">
  <li>Ut enim ad minim veniam, quis nostrud exercitation.</li>
  <li>Lorem ipsum dolor sit amet, consectetur adipiscing elit.</li>
  <li>Ut enim ad minim veniam, quis nostrud exercitation.</li>
  <li>Lorem ipsum dolor sit amet, consectetur adipiscing elit.</li>
  <li>Ut enim ad minim veniam, quis nostrud exercitation.</li>
</ul>
<div class="abs" role="img" aria-label="Illustration of a woman pointing at large analytics dashboards" style="left:607px;top:1536px;width:506px;height:469px;border-radius:50%;background:radial-gradient(circle,#3b60d8 0%,#26337f 45%,#22184f 70%)"></div>

<section class="abs cta">
  <div class="label" style="margin-top:88px">Offer Special For You</div>
  <h2 style="margin-top:18px;line-height:55px">We will take you to even more amazing<br>success. Are you interested?</h2>
  <a class="btn" style="width:156px;height:44px;margin-top:24px">
    <svg width="15" height="15" viewBox="0 0 24 24"><path d="M5 3h4l2 5-3 2a11 11 0 0 0 6 6l2-3 5 2v4a2 2 0 0 1-2 2A17 17 0 0 1 3 5a2 2 0 0 1 2-2z" stroke="#fff" stroke-width="1.8" fill="none"/></svg>Call Us Now</a>
</section>

<div class="abs label" style="left:0;width:1200px;text-align:center;top:2522px">Portfolio</div>
<h2 class="abs" style="left:0;width:1200px;text-align:center;top:2556px;font-size:38px">Here are Some of Our Works</h2>
<section class="abs works">
  <div class="tile" role="img" aria-label="Photo of analytics charts on screen under a magenta overlay" style="background:linear-gradient(160deg,#c41aa6,#a21ab8 55%,#8a1cc4);justify-content:flex-start;padding-top:178px">
    <h4>Micro Service Data Analyst</h4>
    <p class="para" style="color:#f0dff5;width:440px;margin-top:10px">Lorem ipsum dolor sit amet, consectetur adipiscing elit, sed do eiusmod tempor incididunt ut labore et dolore magna aliqua. Ut enim ad minim veniam, quis nostrud exercitation ullamco laboris nisi.</p>
    <a class="btn" style="background:#1a0b3c;width:156px;height:42px;margin-top:18px">See Details
      <svg width="14" height="10" viewBox="0 0 14 10"><path d="M1 5h11M8 1l4 4-4 4" stroke="#fff" stroke-width="1.6" fill="none"/></svg></a>
  </div>
  <div class="tile" role="img" aria-label="Photo of a trading screen with metrics" style="background:linear-gradient(180deg,#3c3d6a 0%,#4a3a78 55%,#d11f9e 100%)"><h4>Nortwell Monthly Analyst</h4></div>
  <div class="tile" role="img" aria-label="Photo of an analyst working on laptops" style="background:linear-gradient(180deg,#2c2a3a 0%,#3a2750 55%,#c91d9f 100%)"><h4>Halvex Yearend Analyst</h4></div>
  <div class="tile" role="img" aria-label="Photo of an analyst reviewing screens" style="background:linear-gradient(180deg,#1e2a5a 0%,#3a2a68 55%,#d11f9e 100%)"><h4>Corvani Analyst</h4></div>
</section>

<div class="abs partners"><span></span><span></span><span></span><span></span><span></span><span></span></div>

<div class="abs contact-bg"></div>
<div class="abs label" style="left:83px;top:4000px">Contact Us</div>
<h2 class="abs" style="left:83px;top:4035px">Request a Quote</h2>
<p class="abs para" style="left:83px;top:4116px;width:505px">Lorem ipsum dolor sit amet, consectetur adipiscing elit, sed do eiusmod tempor incididunt ut labore et dolore magna aliqua. Ut enim ad minim veniam, quis nostrud exercitation ullamco laboris nisi ut aliquip ex ea commodo consequat. Duis aute irure dolor in reprehenderit in voluptate velit esse cillum dolore eu fugiat nulla pariatur. Excepteur sint occaecat cupidatat non proident, sunt in culpa qui officia deserunt mollit anim id est laborum.</p>

<form>
  <label class="abs field-label" style="left:613px;top:4004px">Full Name</label>
  <div class="abs field" style="left:613px;top:4024px;width:238px;height:42px"></div>
  <label class="abs field-label" style="left:876px;top:4004px">Email Address</label>
  <div class="abs field" style="left:876px;top:4024px;width:239px;height:42px"></div>
  <label class="abs field-label" style="left:613px;top:4088px">Message</label>
  <div class="abs field" style="left:613px;top:4110px;width:502px;height:168px"></div>
  <a class="abs btn" style="left:613px;top:4304px;width:189px;height:44px">Submit Message
    <svg width="14" height="10" viewBox="0 0 14 10"><path d="M1 5h11M8 1l4 4-4 4" stroke="#fff" stroke-width="1.6" fill="none"/></svg></a>
</form>

<div class="abs brand" style="left:83px;top:4536px"><span>BRIGHTMERE</span><span class="dot"></span></div>
<div class="abs" style="left:347px;top:4520px;font-size:18px;font-weight:700">Brightmere</div>
<p class="abs para" style="left:347px;top:4550px;width:480px">Lorem ipsum dolor sit amet, consectetur adipiscing elit, sed do eiusmod tempor incididunt ut labore et dolore magna aliqua.</p>
<div class="abs social" style="left:970px;top:4543px"><span></span><span style="background:none;border:1.5px solid #fff;border-radius:50%"></span><span style="background:none;border:1.5px solid #fff"></span><span style="background:none;border:1.5px solid #fff"></span></div>
<div class="abs" style="left:0;width:1200px;text-align:center;top:4700px;font-size:12px;color:var(--muted)">© 2023 <span style="color:var(--magenta)">Pinecrest Studio</span> All Rights Reserved</div>

</body>
</html>
```